Tri-fold Brochure Design for Banking Business

The brochure we have needs to be improved - more business like and more attractive. Logo file and brochure is attached. I would like to be able to edit the text after you get done. Your ideas and changes to text are welcome. See our website www.korvanbridgegrp.com for our theme. We can use indesign to edit the text after you complete. However, please make changes to the text we have in the design that it uploaded. Your comments and changes are welcome.

Target Market(s)

Human Resources and learning & development staff at the global investment banks - Pellham Trask, QWNR, etc.

Industry/Entity Type

Investment Banking

Logo Text

Korvan Bridge Group

Font styles to use
Serif
Sans Serif

Colors
33a6d7
0493ce
3277b5
fbf289
fdf9cf
fbee3e
0555a3
85acd3

Requirements
Must have
• Must be similar to our website www.korvanbridgegrp.com. Needs to be business-like, clean fonts, sharp design. Our logo - of course.
Nice to have
• City images - seems to be our theme.

```html
<!DOCTYPE html>
<html lang="en">
<head>
<meta charset="utf-8">
<title>Korvan Bridge Group – Tri-fold Brochure</title>
<link href="https://fonts.googleapis.com/css2?family=Open+Sans:wght@400;600;700&family=Saira+Semi+Condensed:wght@500;600;700&display=swap" rel="stylesheet">
<style>
  :root{
    --page-bg:#b4b4b4;
    --paper:#ffffff;
    --brand-blue:#0555a3;
    --mid-blue:#3277b5;
    --bright-blue:#0493ce;
    --sky-top:#e9f1fb;
    --sky-mid:#9fbfe2;
    --water:#4f7fae;
    --yellow:#fbee3e;
    --ink:#1d1d1f;
    --text:#4a4a4a;
    --map-grey:#d3d5d8;
  }
  *{box-sizing:border-box;margin:0;padding:0}
  html,body{width:1200px;height:1200px;overflow:hidden}
  body{background:var(--page-bg);font-family:"Open Sans",Arial,sans-serif;color:var(--text)}
  .spread{position:absolute;left:30px;top:160px;width:1140px;height:880px;display:flex;box-shadow:0 18px 40px rgba(0,0,0,.25)}
  .panel{position:relative;width:380px;height:880px;background:var(--paper);overflow:hidden}
  .panel + .panel{border-left:1px solid #e2e4e8}
  .panel svg.art{position:absolute;left:0;top:0}
  .heading{font-family:"Saira Semi Condensed","Arial Narrow",sans-serif;font-weight:600;color:var(--brand-blue)}
  /* about panel */
  .about{padding:30px 26px 0 26px}
  .about .heading{font-size:21px;margin-bottom:14px}
  .about p{font-size:11.2px;line-height:1.45;text-align:justify;margin-bottom:12px}
  .about p.inset{text-align:right;margin-left:40px}
  /* brand name */
  .brand{display:flex;align-items:center;gap:10px}
  .brand-mark{width:20px;height:20px;background:var(--brand-blue);flex:none}
  .brand-name{font-family:"Saira Semi Condensed","Arial Narrow",sans-serif;font-weight:600;color:var(--ink);font-size:22px;line-height:1;letter-spacing:1px;text-transform:uppercase;white-space:nowrap}
  /* contact panel */
  .world-map{position:absolute;left:20px;top:40px;width:340px;height:190px;background:radial-gradient(ellipse at center,var(--map-grey) 0%,#e6e7e9 60%,transparent 75%)}
  .tagline-service{position:absolute;top:262px;left:0;width:380px;text-align:center;font-weight:600;font-size:18px;color:#333}
  .contact .brand{position:absolute;top:318px;left:0;width:380px;justify-content:center}
  .contact-list{position:absolute;top:410px;left:30px;list-style:none}
  .contact-list li{margin-bottom:22px;font-size:11.5px}
  .contact-list .region{display:flex;align-items:center;gap:8px;font-weight:700;color:var(--brand-blue);font-size:11.5px}
  .contact-list .addr{margin-left:24px}
  .icon{width:15px;height:12px;flex:none}
  .contact-us{position:absolute;top:650px;left:30px;width:260px}
  .contact-us .heading{font-size:17px}
  .contact-us .sub{color:var(--mid-blue);font-size:12px;font-family:"Saira Semi Condensed","Arial Narrow",sans-serif;margin-bottom:10px}
  .row{display:flex;align-items:flex-start;gap:8px;font-size:11px;margin-bottom:10px;white-space:nowrap}
  .row.indent{margin-left:10px}
  .phones{display:flex;gap:14px;margin-left:22px;font-size:11px;white-space:nowrap}
  .phones span{display:flex;align-items:center;gap:6px}
  .web{margin:14px 0 0 34px;font-weight:700;letter-spacing:1px;font-size:11px;color:#333;display:flex;align-items:center;gap:8px;white-space:nowrap}
  /* cover panel */
  .cover .brand{position:absolute;top:50px;left:34px}
  .cover .city-photo{position:absolute;left:0;top:140px;width:380px;height:430px;background:linear-gradient(180deg,var(--sky-top) 0%,var(--sky-mid) 45%,#5a7fa8 72%,var(--water) 82%,#6f92b8 100%)}
  .cover-tagline{position:absolute;right:26px;top:690px;text-align:right;font-family:"Saira Semi Condensed","Arial Narrow",sans-serif;line-height:1.2;white-space:nowrap}
  .cover-tagline .lead{font-size:22px;font-weight:500;color:#555}
  .cover-tagline .strong{font-size:22px;font-weight:700;color:var(--bright-blue);text-transform:uppercase}
  .cover-web{position:absolute;right:26px;top:790px;font-weight:700;font-size:11px;letter-spacing:1.2px;color:#333;text-transform:uppercase}
</style>
</head>
<body>
<main class="spread">

  <section class="panel about">
    <h2 class="heading">ABOUT US</h2>
    <p>Korvan Bridge Group's dedicated staff is able to efficiently provide complete sales, marketing and logistical support for all our programs, no matter the location. Our globally located trainers have extensive experience, both as industry professionals and as trainers. Their efforts are complemented by our highly trained logistical support team supported by the latest shared workspace, scheduling and customer management systems.</p>
    <p>Korvan Bridge Group efficiently provides complete sales, marketing and logistical support for all our programs, no matter the location.</p>
    <p class="inset">Our globally located trainers have extensive experience, both as industry professionals and as trainers.</p>
    <p class="inset">Our highly qualified logistical team complement the training services, providing reliable and efficient support.</p>
    <svg class="art" width="380" height="880" viewBox="0 0 380 880" aria-hidden="true">
      <polygon points="0,330 0,390 260,860 330,860" fill="#0555a3"/>
      <polygon points="0,390 0,460 200,860 260,860" fill="#3277b5"/>
      <rect x="0" y="862" width="380" height="8" fill="#fbee3e"/>
      <rect x="0" y="870" width="380" height="10" fill="#0555a3"/>
    </svg>
    <svg class="art" width="380" height="880" viewBox="0 0 380 880" role="img" aria-label="Photo of a glass skyscraper spire among city buildings">
      <defs>
        <linearGradient id="towerPhoto" x1="0" y1="0" x2="0" y2="1">
          <stop offset="0" stop-color="#dfe7ef"/>
          <stop offset=".55" stop-color="#8ea7bd"/>
          <stop offset="1" stop-color="#3f5a6e"/>
        </linearGradient>
      </defs>
      <polygon points="0,460 200,860 0,860" fill="url(#towerPhoto)"/>
    </svg>
  </section>

  <section class="panel contact">
    <div class="world-map" role="img" aria-label="Light grey world map"></div>
    <h3 class="tagline-service">Worldwide Training Service</h3>
    <div class="brand"><span class="brand-mark"></span><span class="brand-name">Korvan Bridge Group</span></div>

    <ul class="contact-list">
      <li><span class="region"><svg class="icon" viewBox="0 0 15 12"><rect x=".5" y=".5" width="14" height="11" fill="#0555a3"/><path d="M1 1l6.5 5L14 1" stroke="#fff" fill="none"/></svg>GLOBAL:</span><div class="addr">elena.rossvik@korvanbridgegrp.com</div></li>
      <li><span class="region"><svg class="icon" viewBox="0 0 15 12"><rect x=".5" y=".5" width="14" height="11" fill="#0555a3"/><path d="M1 1l6.5 5L14 1" stroke="#fff" fill="none"/></svg>ASIA:</span><div class="addr">owen.barclift@korvanbridgegrp.com</div></li>
      <li><span class="region"><svg class="icon" viewBox="0 0 15 12"><rect x=".5" y=".5" width="14" height="11" fill="#0555a3"/><path d="M1 1l6.5 5L14 1" stroke="#fff" fill="none"/></svg>UNITED STATES:</span><div class="addr">paul.merrow@korvanbridgegrp.com</div></li>
      <li><span class="region"><svg class="icon" viewBox="0 0 15 12"><rect x=".5" y=".5" width="14" height="11" fill="#0555a3"/><path d="M1 1l6.5 5L14 1" stroke="#fff" fill="none"/></svg>EUROPE:</span><div class="addr">neil.castor@korvanbridgegrp.com</div></li>
    </ul>

    <svg class="art" width="380" height="880" viewBox="0 0 380 880" aria-hidden="true">
      <polygon points="300,700 380,700 380,880" fill="#0555a3"/>
      <polygon points="330,700 350,700 380,770 380,800" fill="#3277b5"/>
    </svg>

    <div class="contact-us">
      <h3 class="heading">CONTACT US :</h3>
      <div class="sub">Our Asia Address</div>
      <div class="row"><svg class="icon" viewBox="0 0 15 12"><path d="M7.5 0L0 6h2v6h4V8h3v4h4V6h2z" fill="#0555a3"/></svg><span>Unit 8C, Harlow Court<br>214-218 Marlin Rd, Eastbay, Harbour City</span></div>
      <div class="row indent"><svg class="icon" viewBox="0 0 15 12"><rect x=".5" y=".5" width="14" height="11" fill="#0555a3"/><path d="M1 1l6.5 5L14 1" stroke="#fff" fill="none"/></svg><span>info@korvanbridgegrp.com</span></div>
      <div class="phones">
        <span><svg class="icon" viewBox="0 0 12 12"><circle cx="6" cy="6" r="5.3" fill="none" stroke="#0555a3"/><path d="M4 3.5l1 1-.6.8c.4.9 1 1.5 1.9 1.9l.8-.6 1 1-.8 1C5.5 8.4 3.6 6.5 3 4.3z" fill="#0555a3"/></svg>+852 5550 1438</span>
        <span><svg class="icon" viewBox="0 0 12 12"><rect x="1" y="4" width="10" height="7" fill="#0555a3"/><rect x="3" y="1" width="6" height="4" fill="none" stroke="#0555a3"/></svg>+852 5550 2716</span>
      </div>
      <div class="web"><svg class="icon" viewBox="0 0 12 12"><circle cx="6" cy="6" r="5.3" fill="none" stroke="#0555a3"/><path d="M.7 6h10.6M6 .7c-3 3-3 7.6 0 10.6M6 .7c3 3 3 7.6 0 10.6" stroke="#0555a3" fill="none"/></svg>WWW.KORVANBRIDGEGRP.COM</div>
    </div>
  </section>

  <section class="panel cover">
    <div class="brand"><span class="brand-mark"></span><span class="brand-name">Korvan Bridge Group</span></div>
    <div class="city-photo" role="img" aria-label="Photo of a harbour city skyline with tall glass towers above the water"></div>
    <svg class="art" width="380" height="880" viewBox="0 0 380 880" aria-hidden="true">
      <polygon points="0,570 380,530 380,590 0,640" fill="#0555a3"/>
      <polygon points="0,640 380,590 380,600 0,655" fill="#fbee3e"/>
      <polygon points="0,655 380,600 380,880 0,880" fill="#ffffff"/>
      <polygon points="0,655 20,652 130,880 60,880 0,760" fill="#0555a3"/>
      <polygon points="20,652 34,650 150,880 130,880" fill="#fbee3e"/>
    </svg>
    <div class="cover-tagline">
      <div class="lead">Your Expert Training and</div>
      <div class="strong">Consulting Partner</div>
    </div>
    <div class="cover-web">www.korvanbridgegrp.com</div>
  </section>

</main>
</body>
</html>
```